Town Planning Consultants require lstationary design

Require a design to be used for our letterhead and report cover page. We have an approved logo.
we have attached our logo, and our temporary letterhead/cover page (SEE Cover) which we currently adapt for both purposes in the interim pending a permanent design. I have also attached an example (example report cover) of a report cover page that I like. perhaps similar with our colour scheme

Target Market(s)

?

Industry/Entity Type

Town

Colors
249fd4
3176b5

Requirements
Must have
• colours to match logo
• the text content in existing letterhead

```html
<!DOCTYPE html>
<html lang="en">
<head>
<meta charset="utf-8">
<title>Kestrel Urban – Report Cover and Letterhead</title>
<link rel="stylesheet" href="https://fonts.googleapis.com/css2?family=Mulish:wght@400;600;700;800&display=swap">
<style>
  :root {
    --brand-blue: #249fd4;
    --brand-deep: #3176b5;
    --ink: #333638;
    --ink-soft: #6f7275;
    --grey-band: #a3a5a7;
    --paper: #ffffff;
    --backdrop: #eeeeee;
    --font: "Mulish", sans-serif;
  }
  * { box-sizing: border-box; margin: 0; padding: 0; }
  html, body { width: 1200px; height: 815px; overflow: hidden; }
  body { background: var(--backdrop); font-family: var(--font); position: relative; color: var(--ink); }

  .sheet { position: absolute; top: 70px; width: 484px; height: 684px; background: var(--paper); box-shadow: 0 2px 8px rgba(0,0,0,.08); overflow: hidden; }
  .report-cover { left: 80px; }
  .letterhead { left: 638px; }

  /* Report cover */
  .cover-header { position: absolute; top: 0; left: 0; right: 0; height: 172px; background: var(--brand-blue); color: #fff; text-align: right; padding: 54px 39px 0 0; }
  .cover-title { font-weight: 800; font-size: 24px; line-height: 32px; letter-spacing: .3px; text-transform: uppercase; }
  .cover-subtitle { font-weight: 400; font-size: 15px; margin-top: 6px; }
  .cover-photo { position: absolute; top: 172px; left: 0; right: 0; height: 302px;
    background: linear-gradient(180deg, #c9d6e6 0%, #dfe6ee 28%, #6f7d5c 42%, #8a8a76 60%, #7e8d80 72%, #8fa39a 100%); }
  .cover-brand { position: absolute; right: 40px; top: 572px; font-weight: 700; font-size: 46px; color: var(--brand-blue); letter-spacing: -.5px; }
  .cover-credits { position: absolute; left: 38px; top: 572px; display: grid; grid-template-columns: 66px auto; row-gap: 1px; font-size: 8.5px; line-height: 10px; color: var(--ink-soft); }
  .cover-credits dt { font-weight: 700; }
  .cover-footer { position: absolute; left: 0; right: 0; bottom: 0; height: 26px; background: var(--grey-band); color: #fff; display: flex; align-items: center; justify-content: space-between; padding: 0 40px 0 38px; font-size: 11px; letter-spacing: .4px; }

  /* Letterhead */
  .letter-brand { position: absolute; left: 40px; top: 60px; font-weight: 700; font-size: 25px; color: var(--brand-blue); letter-spacing: -.3px; }
  .letter-contact { position: absolute; left: 368px; top: 54px; font-size: 6.8px; line-height: 8.8px; color: var(--ink); }
  .letter-contact .label { color: var(--brand-blue); font-weight: 700; }
  .letter-contact address { font-style: normal; margin-top: 5px; }
  .letter-body { position: absolute; left: 40px; top: 167px; width: 404px; font-size: 6.8px; line-height: 8.8px; color: var(--ink); }
  .letter-date { margin-bottom: 12px; }
  .letter-recipient { font-style: normal; margin-bottom: 39px; }
  .letter-salutation { font-weight: 700; margin-bottom: 9px; }
  .letter-body p { text-align: justify; margin-bottom: 9px; }
  .letter-signoff { margin-top: 14px; display: flex; align-items: flex-start; gap: 8px; }
  .letter-signoff strong { display: block; }
  .signature-area { width: 100px; height: 36px; margin-top: -4px; background: linear-gradient(90deg, rgba(49,118,181,.08), rgba(49,118,181,.16)); border-radius: 3px; }
  .letter-footer { position: absolute; left: 39px; bottom: 18px; font-size: 8px; font-weight: 700; color: var(--ink-soft); letter-spacing: .3px; display: flex; gap: 6px; }
  .letter-footer .divider { color: var(--brand-blue); }
  .letter-rule { position: absolute; left: 0; right: 0; bottom: 0; height: 8px; background: linear-gradient(90deg, var(--grey-band) 0 66%, var(--brand-blue) 66% 100%); }
</style>
</head>
<body>

<article class="sheet report-cover">
  <header class="cover-header">
    <h1 class="cover-title">Statement of<br>Environmental Effects</h1>
    <p class="cover-subtitle">Proposed Additions to Existing Dwelling</p>
  </header>
  <div class="cover-photo" role="img" aria-label="Photograph of waterfront homes among trees above a harbour with moored boats"></div>
  <dl class="cover-credits">
    <dt>Prepared for:</dt><dd>R.Callander</dd>
    <dt>Prepared by:</dt><dd>T.Marsh</dd>
    <dt>Reviewed by:</dt><dd>L.Brandt</dd>
    <dt>Dated:</dt><dd>June, 2016</dd>
  </dl>
  <div class="cover-brand">Kestrel Urban</div>
  <footer class="cover-footer">
    <span>PLANNING</span><span>|</span><span>DEVELOPMENT</span><span>|</span><span>URBAN DESIGN</span><span>|</span><span>CONSULTANTS</span>
  </footer>
</article>

<article class="sheet letterhead">
  <div class="letter-brand">Kestrel Urban</div>
  <div class="letter-contact">
    <div><span class="label">T:</span> +61 (2) 5550 1420</div>
    <div><span class="label">M:</span> +61 (0) 400 555 218</div>
    <div><span class="label">E:</span> office@kestrelurban.com.au</div>
    <address>12 Harbour Ridge Road,<br>TALLOWVALE&nbsp; NSW 2490</address>
  </div>

  <div class="letter-body">
    <div class="letter-date">30.09.2015</div>
    <address class="letter-recipient">Recipient's name<br>Seeblick 12<br>10439 Berlin<br>Germany</address>
    <div class="letter-salutation">Dear sir,</div>
    <p>Clear communication sits at the centre of every planning project we undertake. Whether a proposal concerns a single dwelling or a new precinct, each stage relies on accurate advice shared between owners, designers, councils and neighbours. Written correspondence keeps that record clear and easy to follow.</p>
    <p>Even with email and messaging, formal letters remain the accepted way to lodge submissions, respond to requests for information and confirm agreed conditions. Councils and agencies continue to rely on signed letters as evidence of advice given, and they are often kept on file for many years after a development is complete.</p>
    <p>A letter also speaks for the firm that sends it. We take care that the language in each letter suits its purpose and audience, and that anything which does not belong in the record is handled separately and with care.</p>
    <p>Should you have any questions about this matter, please contact our office. We would be pleased to discuss the proposal further and to arrange a meeting at a time that suits you.</p>
    <div class="letter-signoff">
      <div>Yours Sincerely,<strong>Elise Morrow</strong></div>
      <div class="signature-area" role="img" aria-label="Handwritten signature"></div>
    </div>
  </div>

  <footer class="letter-footer">
    <span>PLANNING</span><span class="divider">|</span><span>DEVELOPMENT</span><span class="divider">|</span><span>URBAN DESIGN</span><span class="divider">|</span><span>CONSULTANTS</span>
  </footer>
  <div class="letter-rule"></div>
</article>

</body>
</html>
```